Film poster for Seven Lanterns Burning - a documentary

We need a poster for our documentary, Seven Lanterns Burning, about how Ancient heroine Antigone finds new life in Beirut’s refugee camps, helping four Syrian women discover the strength to live with joy through the greatest of tragedies. The film is about 20% animated with the rest being vérité footage shot in Beirut, Lebanon. The title will be in Arabic and English.

Please check out our trailer here: https://www.fundmorrow.com/projects/461830527/seven-lanterns-burning?ref=tapzq3

We've included some assets from the film as well as style references of other film posters we've liked.

The designer we use will also get a credit in the film.

Target Market(s)

Documentary film festivals

Industry/Entity Type

Film Production

Font styles to use
Sans Serif

Colors

Designer to choose colors to be used in the design.

Requirements
Must have
• The Title in Both English and Arabic (Can provide the text for the arabic)
• Space at the bottom to overlay film credits
Nice to have
• Include the texture of the wall and perhaps integrate both photographic and graphic imagery
Should not have
• Shouldn't be too busy - minimalistic

```html
<!DOCTYPE html>
<html lang="en">
<head>
<meta charset="UTF-8">
<title>Seven Lanterns Burning — Poster</title>
<link rel="stylesheet" href="https://fonts.googleapis.com/css2?family=Anton&family=Oswald:wght@500&family=Cairo:wght@700&display=swap">
<style>
  :root {
    --page: #ffffff;
    --ink: #000000;
    --title: #ffffff;
    --accent: #c8202a;
    --wall-light: #8a7d66;
    --wall-mid: #6e4a34;
    --wall-dark: #4a3222;
    --star-light: #cfcdd0;
    --star-mid: #a08570;
    --star-dark: #3a2b22;
  }
  html, body {
    margin: 0;
    width: 1200px;
    height: 1200px;
    overflow: hidden;
    background: var(--page);
  }
  .poster {
    position: absolute;
    left: 288px;
    top: 98px;
    width: 624px;
    height: 1004px;
    background: var(--ink);
    overflow: hidden;
  }
  .poster__artwork {
    position: absolute;
    left: 0;
    top: 0;
    width: 624px;
    height: 501px;
    display: block;
  }
  .poster__arabic-title {
    position: absolute;
    left: 12px;
    top: 418px;
    width: 600px;
    margin: 0;
    text-align: center;
    font-family: "Cairo", sans-serif;
    font-weight: 700;
    font-size: 48px;
    line-height: 1;
    color: rgba(255, 255, 255, 0.32);
    white-space: nowrap;
  }
  .poster__title {
    position: absolute;
    left: 0;
    top: 506px;
    width: 624px;
    margin: 0;
    text-align: center;
    font-family: "Anton", sans-serif;
    font-weight: 400;
    font-size: 72px;
    line-height: 0.92;
    letter-spacing: -0.5px;
    color: var(--title);
    text-transform: uppercase;
  }
  .poster__tagline {
    position: absolute;
    left: 0;
    top: 664px;
    width: 624px;
    margin: 0;
    text-align: center;
    font-family: "Oswald", sans-serif;
    font-weight: 500;
    font-size: 14px;
    letter-spacing: 0.2px;
    color: var(--accent);
    text-transform: uppercase;
  }
</style>
</head>
<body>
  <main class="poster">
    <svg class="poster__artwork" viewBox="0 0 624 501" xmlns="http://www.w3.org/2000/svg">
      <defs>
        <linearGradient id="wall" x1="0" y1="0" x2="1" y2="1">
          <stop offset="0" stop-color="var(--wall-light)"/>
          <stop offset="0.45" stop-color="var(--wall-mid)"/>
          <stop offset="1" stop-color="var(--wall-dark)"/>
        </linearGradient>
        <linearGradient id="portrait" x1="0" y1="0" x2="1" y2="0">
          <stop offset="0" stop-color="var(--star-light)"/>
          <stop offset="0.6" stop-color="var(--star-mid)"/>
          <stop offset="1" stop-color="var(--star-dark)"/>
        </linearGradient>
      </defs>
      <rect class="wall-texture" width="624" height="501" fill="url(#wall)" role="img" aria-label="Weathered, peeling plaster wall texture"/>
      <polygon class="star-window" role="img" aria-label="Photograph of a young woman in a white headscarf gazing into the distance"
        fill="url(#portrait)"
        points="314,0 236,192 64,192 200,346 184,501 314,414 468,501 420,350 564,192 412,192"/>
    </svg>

    <p class="poster__arabic-title" lang="ar" dir="rtl">سبعة فوانيس مشتعلة</p>
    <h1 class="poster__title">Seven Lanterns<br>Burning</h1>
    <p class="poster__tagline">A film about live, love and Syria.</p>
  </main>
</body>
</html>
```